Invitation

Please design an invitation for March 31st drop in between 10-1 reception to celebrate the opening of Hartwell's Landing and the Residences at 8 N. Birch. 8 N. Birch Street Quarryville, PA 17593. Tour the buildings newly renovated units and commercial space and enjoy refreshments at the reception.

```html
<!DOCTYPE html>
<html lang="en">
<head>
<meta charset="utf-8">
<title>Grand Opening Invitation – Hartwell's Landing</title>
<link rel="stylesheet" href="https://fonts.googleapis.com/css2?family=Lato:wght@300;400;700&display=swap">
<style>
  :root {
    --teal: #13917b;
    --teal-deep: #0f6f70;
    --teal-dark: #0d5f66;
    --mist: #eef5f2;
    --ink: #222526;
    --ink-soft: #3b3f41;
    --paper: #ffffff;
    --stage: #ffffff;
  }
  * { margin: 0; padding: 0; box-sizing: border-box; }
  html, body { width: 1200px; height: 1200px; overflow: hidden; background: var(--stage); }
  body { font-family: "Lato", sans-serif; color: var(--ink); }

  .invitation {
    position: absolute; left: 217px; top: 0;
    width: 766px; height: 1200px;
    overflow: hidden; background: var(--mist);
  }
  .invitation__backdrop { position: absolute; inset: 0; }

  .snapshot {
    position: absolute; left: 23px; width: 228px; height: 212px;
    background: var(--paper);
    box-shadow: 0 3px 8px rgba(0,0,0,.18);
  }
  .snapshot--birch { top: 680px; }
  .snapshot--elm { top: 929px; }
  .snapshot__photo {
    position: absolute; left: 7px; top: 8px; width: 214px; height: 168px;
    background: linear-gradient(180deg, #b9c7d6 0%, #d9dde2 35%, #7d7f78 62%, #3a3a3c 100%);
  }
  .snapshot__label {
    position: absolute; left: 0; right: 0; bottom: 9px;
    text-align: center; font-weight: 700; font-size: 17px;
    color: var(--teal); letter-spacing: .2px;
  }

  .brand {
    position: absolute; left: 463px; top: 618px; width: 252px; height: 66px;
    display: flex; align-items: center; justify-content: center; gap: 10px;
  }
  .brand__mark { width: 16px; height: 16px; background: var(--teal-deep); }
  .brand__name { font-size: 24px; font-weight: 400; color: var(--ink-soft); white-space: nowrap; }

  .invite-copy {
    position: absolute; left: 311px; width: 410px;
    font-size: 19.5px; font-weight: 300; line-height: 26.3px;
    text-align: justify; color: var(--ink);
  }
  .invite-copy strong { font-weight: 700; }
  .invite-copy--lead { top: 712px; }
  .invite-copy--tour { top: 868px; text-align: left; }

  .contact { position: absolute; left: 290px; top: 1026px; color: #fff; }
  .contact__title { font-size: 22px; font-weight: 700; margin-bottom: 10px; }
  .contact__row {
    position: absolute; display: flex; align-items: flex-start; gap: 8px;
    font-size: 16.5px; line-height: 21.5px; white-space: nowrap;
  }
  .contact__row svg { width: 16px; height: 16px; margin-top: 3px; flex: none; }
  .row-address { left: 0; top: 44px; }
  .row-email { left: 0; top: 88px; }
  .row-web { left: 0; top: 126px; }
  .row-phone { left: 303px; top: 44px; }
  .row-fax { left: 303px; top: 66px; }
</style>
</head>
<body>
<main class="invitation">
  <svg class="invitation__backdrop" viewBox="0 0 766 1200" width="766" height="1200" aria-hidden="true">
    <defs>
      <linearGradient id="mistFade" x1="0" y1="0" x2="0" y2="1">
        <stop offset="0" stop-color="#e9f3ef"/>
        <stop offset="0.5" stop-color="#ffffff"/>
        <stop offset="1" stop-color="#eef5f2"/>
      </linearGradient>
      <linearGradient id="tealSweep" x1="0" y1="0" x2="1" y2="0">
        <stop offset="0" stop-color="#0f7f78"/>
        <stop offset="1" stop-color="#13927b"/>
      </linearGradient>
      <linearGradient id="footSweep" x1="0" y1="0" x2="1" y2="1">
        <stop offset="0" stop-color="#13917b"/>
        <stop offset="1" stop-color="#0e6e70"/>
      </linearGradient>
      <linearGradient id="heroTones" x1="0" y1="0" x2="0" y2="1">
        <stop offset="0" stop-color="#8fa9c9"/>
        <stop offset="0.3" stop-color="#c8d2dd"/>
        <stop offset="0.55" stop-color="#8a8d86"/>
        <stop offset="0.78" stop-color="#b9b7b2"/>
        <stop offset="1" stop-color="#2f2b2e"/>
      </linearGradient>
    </defs>
    <rect width="766" height="1200" fill="url(#mistFade)"/>
    <!-- upper teal wave -->
    <path d="M0 440 L766 280 L766 520 C620 545 470 560 330 600 C200 636 90 660 0 662 Z" fill="url(#tealSweep)"/>
    <path d="M560 520 C640 510 710 505 766 500 L766 522 C700 524 630 528 560 535 Z" fill="var(--teal-dark)" opacity=".7"/>
    <!-- hero photo area -->
    <path role="img" aria-label="Rendering of the renovated corner building with storefront windows, porch and street under a cloudy sky"
          d="M0 0 H766 V305 C680 400 580 470 470 510 C380 540 280 545 190 530 C110 516 50 490 0 463 Z" fill="url(#heroTones)"/>
    <!-- lower teal band -->
    <path d="M0 1005 C260 1005 560 1000 766 940 L766 1200 L0 1200 Z" fill="url(#footSweep)"/>
  </svg>

  <figure class="snapshot snapshot--birch">
    <div class="snapshot__photo" role="img" aria-label="Photo of the building frontage along Birch Street"></div>
    <figcaption class="snapshot__label">BIRCH STREET</figcaption>
  </figure>
  <figure class="snapshot snapshot--elm">
    <div class="snapshot__photo" role="img" aria-label="Photo of the building corner and porch along Elm Street"></div>
    <figcaption class="snapshot__label">ELM STREET</figcaption>
  </figure>

  <div class="brand">
    <span class="brand__mark"></span>
    <span class="brand__name">Bramblewood Properties</span>
  </div>

  <p class="invite-copy invite-copy--lead"><strong>Bramblewood Properties</strong> invites you to the Grand Opening of <strong>Hartwell's Landing and the Residences</strong>. A Celebration will be held on the 31st of March between 10am to 1pm at <strong>8 N. Birch Street Quarryville, PA 17593.</strong></p>
  <p class="invite-copy invite-copy--tour">Tour the Buildings newly renovated units and commercial space and enjoy refreshments at the venue.</p>

  <section class="contact">
    <h2 class="contact__title">Get in Touch:</h2>
    <div class="contact__row row-address">
      <svg viewBox="0 0 16 16"><path d="M8 1a5 5 0 0 0-5 5c0 4 5 9 5 9s5-5 5-9a5 5 0 0 0-5-5zm0 7a2 2 0 1 1 0-4 2 2 0 0 1 0 4z" fill="#fff"/></svg>
      <span>2240 Orchard Road<br>Quarryville, PA 17593</span>
    </div>
    <div class="contact__row row-email">
      <svg viewBox="0 0 16 16"><rect x="1" y="3.5" width="14" height="9" fill="#fff"/><path d="M1.5 4 L8 9 L14.5 4" stroke="#13917b" stroke-width="1.3" fill="none"/></svg>
      <span>hello@bramblewoodproperties.com</span>
    </div>
    <div class="contact__row row-web">
      <svg viewBox="0 0 16 16" fill="none" stroke="#fff" stroke-width="1.2"><circle cx="8" cy="8" r="6.5"/><ellipse cx="8" cy="8" rx="3" ry="6.5"/><path d="M1.5 8h13M2.5 5h11M2.5 11h11"/></svg>
      <span>www.bramblewoodproperties.com</span>
    </div>
    <div class="contact__row row-phone">
      <svg viewBox="0 0 16 16"><path d="M3.5 1.5l2.5 0 1 3.5-1.7 1.2c.8 1.8 2.2 3.2 4 4l1.2-1.7 3.5 1v2.5c0 .8-.7 1.5-1.5 1.5C6.8 13.5 2 8.7 2 3c0-.8.7-1.5 1.5-1.5z" fill="#fff"/></svg>
      <span>717.555.0142</span>
    </div>
    <div class="contact__row row-fax">
      <svg viewBox="0 0 16 16"><rect x="4" y="1.5" width="8" height="4" fill="#fff"/><rect x="1.5" y="6" width="13" height="6" rx="1" fill="#fff"/><rect x="4" y="10" width="8" height="4.5" fill="#fff" stroke="#13917b" stroke-width="1"/></svg>
      <span>717.555.0187</span>
    </div>
  </section>
</main>
</body>
</html>
```